Manuka honey wholesales and exports

We need business cards for our honey distribution company based in New Zealand. We supply shops locally and export Manuka honey around the world.
We deal with a very high quality and 100% natural product that can be used for medical, general health as well as food. We are looking business cards that show our honey products are of a high quality with a modern look.

Target Market(s)

Health and medical retailers and importers

Industry/Entity Type

Wholesale

Contact Information for Business Card

Tevin Apiary NZ Limited

www.tevinapiarynz.example

Derek Fawley

M +64 219036482

E tevinapiarynz@mailbox.example

PO Box 58-214
Takapuna
North Shore
Auckland
New Zealand

Font styles to use
Serif

Requirements
Must have
• (Tevin Apiary NZ Limited) with some artwork on one side and all details on the other side.
Nice to have
• I have seen a very simple card with large yellow and black stripes on one side with a company name.. looked clean and simple so something similar or just let the creative beast inside you take over and we will see what you can come up with.

```html
<!DOCTYPE html>
<html lang="en">
<head>
<meta charset="utf-8">
<title>Tevin Apiary NZ Limited — Business Cards</title>
<link rel="stylesheet" href="https://fonts.googleapis.com/css2?family=Tinos:wght@400;700&display=swap">
<style>
  :root {
    --honey: #ffd84d;
    --honey-light: #ffe978;
    --honey-deep: #fbbd2a;
    --ink: #111111;
    --grey: #6d6d6d;
    --divider: #c9c9c9;
    --paper: #ffffff;
    --backdrop: #1b1b1b;
  }
  * { margin: 0; padding: 0; box-sizing: border-box; }
  html, body {
    width: 1200px; height: 948px; overflow: hidden;
    background: var(--backdrop);
    font-family: "Tinos", "Times New Roman", serif;
    color: var(--ink);
  }
  .canvas { position: relative; width: 1200px; height: 948px; }

  .card { position: absolute; width: 627px; height: 358px; overflow: hidden; }

  /* Front */
  .card-front {
    left: 67px; top: 183px;
    background: radial-gradient(circle at 53% 45%, var(--honey-light) 0%, var(--honey) 45%, #ffd54a 100%);
  }
  .brand-mark {
    position: absolute; width: 67px; height: 67px; border-radius: 50%;
    background: var(--ink);
  }
  .card-front .brand-mark { left: 302px; top: 118px; }
  .brand-name {
    position: absolute; white-space: nowrap;
    font-weight: 700; font-size: 18px; color: var(--ink);
    transform: translateX(-50%);
  }
  .card-front .brand-name { left: 336px; top: 204px; }
  .front-web {
    position: absolute; left: 0; width: 100%; top: 276px;
    text-align: center; font-size: 11px; letter-spacing: 9.4px;
    text-indent: 9.4px; color: var(--ink);
  }

  /* Back */
  .card-back {
    left: 553px; top: 561px; background: var(--paper);
  }
  .card-back .brand-mark { left: 75px; top: 120px; }
  .card-back .brand-name { left: 116px; top: 208px; font-size: 17px; }
  .divider {
    position: absolute; left: 222px; top: 70px; width: 2px; height: 240px;
    background: var(--divider);
  }
  .back-web {
    position: absolute; right: 24px; top: 22px;
    font-size: 15.5px; color: var(--grey);
  }
  .holder-name {
    position: absolute; left: 249px; top: 86px;
    font-size: 26px; font-weight: 700; letter-spacing: 0.3px;
  }
  .contact-row { position: absolute; left: 254px; display: flex; align-items: flex-start; }
  .contact-row svg { width: 11px; height: 13px; margin-top: 3px; flex: none; }
  .contact-row .value { margin-left: 12px; font-size: 14.5px; line-height: 17.5px; }
  .row-address { top: 140px; }
  .row-phone { top: 241px; }
  .row-phone .value { font-size: 19px; font-weight: 700; line-height: 22px; }
  .row-phone svg { margin-top: 5px; }
  .row-email { top: 284px; }
  .row-email svg { margin-top: 4px; }
  .base-band {
    position: absolute; left: 0; bottom: 0; width: 100%; height: 27px;
    background: var(--honey);
  }
</style>
</head>
<body>
<main class="canvas">
  <section class="card card-front">
    <div class="brand-mark"></div>
    <div class="brand-name">Tevin Apiary NZ Limited</div>
    <div class="front-web">www.tevinapiarynz.example</div>
  </section>

  <section class="card card-back">
    <div class="back-web">www.tevinapiarynz.example</div>
    <div class="brand-mark"></div>
    <div class="brand-name">Tevin Apiary NZ Limited</div>
    <div class="divider"></div>

    <h1 class="holder-name">Derek Fawley</h1>

    <div class="contact-row row-address">
      <svg viewBox="0 0 11 13" aria-hidden="true"><path d="M5.5 0C2.5 0 .5 2.2.5 4.8c0 3 5 8.2 5 8.2s5-5.2 5-8.2C10.5 2.2 8.5 0 5.5 0zm0 6.8a2 2 0 1 1 0-4 2 2 0 0 1 0 4z" fill="var(--honey-deep)"/></svg>
      <div class="value">PO Box 58-214<br>Takapuna<br>North Shore<br>Auckland<br>New Zealand</div>
    </div>

    <div class="contact-row row-phone">
      <svg viewBox="0 0 11 13" aria-hidden="true"><rect x="2" y="0.8" width="7" height="11.4" rx="1.2" fill="none" stroke="var(--honey-deep)" stroke-width="1.3"/><rect x="4.3" y="10" width="2.4" height="0.9" fill="var(--honey-deep)"/></svg>
      <div class="value">+64 219036482</div>
    </div>

    <div class="contact-row row-email">
      <svg viewBox="0 0 11 13" aria-hidden="true"><rect x="0" y="3" width="11" height="7.5" fill="var(--honey-deep)"/><path d="M0 3l5.5 4L11 3" fill="none" stroke="#fff" stroke-width="1"/></svg>
      <div class="value">tevinapiarynz@mailbox.example</div>
    </div>

    <div class="base-band"></div>
  </section>
</main>
</body>
</html>
```